Business Card - Cooperate

Business Card for Larkfield Management Consulting

Target Market(s)

Corparte - b2B

Industry/Entity Type

Management Consulting - Professional Services

Contact Information for Business Card

Company Name , Slogan , Dummy Address,

Requirements
Must have
• Reach your Full Potential

```html
<!DOCTYPE html>
<html lang="en">
<head>
<meta charset="utf-8">
<title>Larkfield Management Consulting – Business Card</title>
<link href="https://fonts.googleapis.com/css2?family=Montserrat:wght@600;700&family=Roboto:wght@400;500&display=swap" rel="stylesheet">
<style>
  :root {
    --backdrop: #d3d6d7;
    --paper: #f3f3f1;
    --navy: #1f2f8c;
    --green: #0f9470;
    --teal-rule: #86d6c3;
    --body-text: #3f4146;
    --edge-green: #137a5c;
  }
  * { margin: 0; padding: 0; box-sizing: border-box; }
  html, body {
    width: 1200px;
    height: 1050px;
    overflow: hidden;
    background: var(--backdrop);
  }
  .canvas {
    position: relative;
    width: 1200px;
    height: 1050px;
  }
  .card {
    position: absolute;
    left: 250px;
    width: 700px;
    height: 400px;
    background: var(--paper);
    box-shadow: 0 10px 28px rgba(0,0,0,0.14);
  }
  .card--back {
    top: 90px;
    border-bottom: 6px solid var(--edge-green);
  }
  .card--front {
    top: 560px;
    border-bottom: 3px solid var(--navy);
  }

  /* Company name */
  .wordmark {
    display: flex;
    align-items: center;
    gap: 14px;
  }
  .wordmark__dot {
    border-radius: 50%;
    background: var(--navy);
    flex: none;
  }
  .wordmark__name {
    font-family: "Montserrat", sans-serif;
    font-weight: 600;
    color: var(--navy);
    line-height: 1;
  }

  /* Slogan: a plain sentence, set apart from the name */
  .slogan {
    font-family: "Roboto", sans-serif;
    font-weight: 400;
    color: var(--green);
    letter-spacing: 0;
  }

  /* Back side */
  .back__brand {
    position: absolute;
    inset: 0;
    display: flex;
    flex-direction: column;
    align-items: center;
    justify-content: center;
  }
  .back__brand .wordmark__dot { width: 46px; height: 46px; }
  .back__brand .wordmark__name { font-size: 76px; }
  .back__slogan {
    position: absolute;
    left: 0;
    right: 0;
    bottom: 40px;
    text-align: center;
    font-size: 18px;
  }

  /* Front side */
  .front__brand {
    position: absolute;
    left: 40px;
    top: 0;
    width: 300px;
    height: 100%;
    display: flex;
    flex-direction: column;
    justify-content: center;
  }
  .front__brand .wordmark { gap: 10px; }
  .front__brand .wordmark__dot { width: 24px; height: 24px; }
  .front__brand .wordmark__name { font-size: 40px; }

  .front__rule {
    position: absolute;
    left: 362px;
    top: 60px;
    width: 1.5px;
    height: 280px;
    background: var(--teal-rule);
  }
  .contact {
    position: absolute;
    left: 390px;
    top: 74px;
    font-family: "Roboto", sans-serif;
    color: var(--body-text);
  }
  .contact__name {
    font-family: "Montserrat", sans-serif;
    font-weight: 700;
    font-size: 20px;
    color: var(--navy);
    text-transform: uppercase;
  }
  .contact__role {
    font-weight: 500;
    font-size: 17px;
    color: var(--green);
    margin-top: 2px;
  }
  .contact__address {
    font-size: 16px;
    line-height: 1.35;
    margin-top: 18px;
  }
  .contact__lines {
    list-style: none;
    margin-top: 12px;
    font-size: 16px;
    line-height: 1.45;
  }
  .contact__lines li {
    display: flex;
    align-items: center;
    gap: 8px;
  }
  .contact__icon {
    width: 14px;
    height: 14px;
    flex: none;
  }
  .contact__icon * { stroke: var(--navy); fill: none; stroke-width: 1.6; }
  .contact__icon .solid { fill: var(--navy); stroke: none; }
  .contact__slogan {
    font-size: 15px;
    margin-top: 16px;
  }
</style>
</head>
<body>
<main class="canvas">

  <section class="card card--back" aria-label="Card back">
    <div class="back__brand">
      <div class="wordmark">
        <span class="wordmark__dot"></span>
        <span class="wordmark__name">larkfield</span>
      </div>
    </div>
    <p class="slogan back__slogan">Reach your full potential.</p>
  </section>

  <section class="card card--front" aria-label="Card front">
    <div class="front__brand">
      <div class="wordmark">
        <span class="wordmark__dot"></span>
        <span class="wordmark__name">larkfield</span>
      </div>
    </div>

    <div class="front__rule"></div>

    <div class="contact">
      <h1 class="contact__name">Martin Caldwell</h1>
      <p class="contact__role">Founder &amp; CEO</p>
      <p class="contact__address">48 Harbor Lane Suite 7<br>Fairview, OR 97024</p>
      <ul class="contact__lines">
        <li>
          <svg class="contact__icon" viewBox="0 0 14 14" aria-hidden="true">
            <path class="solid" d="M3 1 L5 1 L6 4 L4.6 5.2 C5.4 7 6.8 8.5 8.8 9.4 L10 8 L13 9 L13 11 C13 12 12 13 11 13 C5.5 12.6 1.4 8.5 1 3 C1 2 2 1 3 1 Z"/>
          </svg>
          <span>555-014-2290</span>
        </li>
        <li>
          <svg class="contact__icon" viewBox="0 0 14 14" aria-hidden="true">
            <rect x="1" y="3" width="12" height="8.5" rx="0.8"/>
            <path d="M1 3.4 L7 8 L13 3.4"/>
          </svg>
          <span>martin@larkfield.com</span>
        </li>
        <li>
          <svg class="contact__icon" viewBox="0 0 14 14" aria-hidden="true">
            <circle cx="7" cy="7" r="5.8"/>
            <ellipse cx="7" cy="7" rx="2.5" ry="5.8"/>
            <path d="M1.2 7 H12.8"/>
          </svg>
          <span>www.larkfield.com</span>
        </li>
      </ul>
      <p class="slogan contact__slogan">Reach your full potential.</p>
    </div>
  </section>

</main>
</body>
</html>
```